Post card

I want an educational customer postcard with our logo, email, and contact number. We are a residential foundation inspection & repair company here in Los Angeles. We provide foundation repair, earthquake retrofitting, and reinforcement.
Our number is 323-555-0148.
Email info@bramblecrestworks.com
Our license number is #2839165

OUR GOAL
Our primary objective is to empower clients with comprehensive knowledge about foundation issues and earthquake retrofitting. By educating them on the potential risks associated with foundation problems and the importance of earthquake retrofitting, we aim to equip homeowners with the necessary information to make informed decisions about safeguarding their properties. Highlighting the benefits of having their houses properly bolted not only enhances structural integrity but also provides peace of mind during seismic events, ensuring the safety and security of their homes and loved ones.

```html
<!DOCTYPE html>
<html lang="en">
<head>
<meta charset="utf-8">
<title>Bramblecrest Works – Postcard</title>
<link rel="stylesheet" href="https://fonts.googleapis.com/css2?family=Arimo:wght@400;700&display=swap">
<style>
  :root{
    --page:#e6e6e6;
    --white:#ffffff;
    --brand-blue:#0a5cf0;
    --deep-blue:#0951c0;
    --brand-red:#d0111f;
    --yellow:#fff200;
    --photo-light:#f4f4f4;
    --photo-mid:#d9d9d9;
    --photo-red:#e0474f;
  }
  *{box-sizing:border-box;margin:0;padding:0}
  html,body{width:1200px;height:1200px;overflow:hidden;background:var(--page)}
  body{position:relative;font-family:"Arimo",Arial,sans-serif}

  .card{position:absolute;width:648px;height:432px;background:var(--white);overflow:hidden}
  .card--red{left:386px;top:124px;--band:var(--brand-red);--stripe:var(--deep-blue);--goal-text:var(--brand-red);--goal-edge:var(--deep-blue);--icon:var(--brand-red)}
  .card--blue{left:166px;top:644px;--band:var(--deep-blue);--stripe:var(--brand-red);--goal-text:var(--deep-blue);--goal-edge:var(--brand-red);--icon:var(--deep-blue)}

  .card__layer{position:absolute;inset:0;width:100%;height:100%}

  .brand{position:absolute;left:27px;top:32px;display:flex;align-items:center;gap:11px}
  .brand__mark{width:40px;height:40px;background:var(--brand-blue);flex:none}
  .brand__name{font-weight:700;font-size:21px;line-height:25px;color:var(--brand-blue);letter-spacing:.3px;white-space:nowrap}

  .goal-tag{position:absolute;left:0;top:169px;width:140px;height:30px;background:var(--yellow);
    border-radius:0 8px 8px 0;box-shadow:4px 0 0 var(--goal-edge);
    font-weight:700;font-size:20px;line-height:30px;padding-left:12px;color:var(--goal-text)}

  .goal-copy{position:absolute;left:12px;top:209px;font-size:14.6px;line-height:16.5px;color:var(--white);white-space:nowrap}

  .contact-title{position:absolute;left:0;right:0;top:359px;display:flex;justify-content:center;align-items:center;gap:6px;
    font-weight:700;font-size:22px;line-height:26px;color:var(--yellow)}
  .contact-title__rule{width:125px;height:9px;
    background:repeating-linear-gradient(to bottom,var(--yellow) 0 2px,transparent 2px 3.5px);}
  .contact-title__rule--left{-webkit-mask:linear-gradient(to right,transparent,#000);mask:linear-gradient(to right,transparent,#000)}
  .contact-title__rule--right{-webkit-mask:linear-gradient(to left,transparent,#000);mask:linear-gradient(to left,transparent,#000)}

  .contact-row{position:absolute;left:78px;top:390px;display:flex;align-items:center;gap:6px;
    font-weight:700;font-size:20px;color:var(--white);white-space:nowrap}
  .contact-row__icon{width:34px;height:26px;flex:none}
  .contact-row__item{display:flex;align-items:center;gap:8px}
</style>
</head>
<body>

<article class="card card--red">
  <svg class="card__layer" viewBox="0 0 1043 694" preserveAspectRatio="none" aria-hidden="true">
    <polygon points="0,171 1043,462 1043,477 0,186" fill="var(--stripe)"/>
    <polygon points="0,186 1043,477 1043,694 0,694" fill="var(--band)"/>
  </svg>
  <svg class="card__layer" viewBox="0 0 1043 694" preserveAspectRatio="none" role="img" aria-label="Photo of a cracked white model house beside an intact red-roofed model house ringed in red on split ground">
    <defs>
      <radialGradient id="photoRed" cx="0.75" cy="0.4" r="0.6">
        <stop offset="0" stop-color="var(--photo-red)" stop-opacity=".35"/>
        <stop offset="1" stop-color="var(--photo-light)" stop-opacity="0"/>
      </radialGradient>
      <linearGradient id="photoBase" x1="0" y1="0" x2="0" y2="1">
        <stop offset="0" stop-color="var(--white)"/>
        <stop offset="1" stop-color="var(--photo-mid)"/>
      </linearGradient>
    </defs>
    <path d="M540,0 C485,125 560,392 800,396 C900,398 990,394 1043,385 L1043,0 Z" fill="url(#photoBase)"/>
    <path d="M540,0 C485,125 560,392 800,396 C900,398 990,394 1043,385 L1043,0 Z" fill="url(#photoRed)"/>
    <path d="M515,0 C455,130 540,408 800,410 C900,411 990,405 1043,396" fill="none" stroke="var(--brand-blue)" stroke-width="9"/>
    <path d="M540,0 C485,125 560,392 800,396 C900,398 990,394 1043,385" fill="none" stroke="var(--brand-red)" stroke-width="6"/>
  </svg>

  <div class="brand">
    <span class="brand__mark"></span>
    <span class="brand__name">BRAMBLECREST<br>WORKS</span>
  </div>

  <div class="goal-tag">OUR GOAL</div>
  <p class="goal-copy">
    Our primary objective is to empower clients<br>
    with comprehensive knowledge about foundation<br>
    issues and earthquake retrofitting. By educating them on the<br>
    potential risks associated with foundation problems and the importance<br>
    of earthquake retrofitting, we aim to equip homeowners with the necessary<br>
    information to make informed decisions about safeguarding their properties.<br>
    Highlighting the benefits of having their houses properly bolted not only enhances structural<br>
    integrity but also provides peace of mind during seismic events, ensuring the safety and<br>
    security of their homes and loved ones.
  </p>

  <div class="contact-title">
    <span class="contact-title__rule contact-title__rule--left"></span>
    <span>CONTACT US</span>
    <span class="contact-title__rule contact-title__rule--right"></span>
  </div>

  <div class="contact-row">
    <span class="contact-row__item">
      <svg class="contact-row__icon" viewBox="0 0 34 26" aria-hidden="true">
        <path d="M0,0 H18 A16,13 0 0 1 18,26 H0 Z" fill="var(--white)"/>
        <path d="M10,7 l3,-1 2,4 -2,1.5 c1,2.5 2.5,4 4.5,5 l1.5,-2 4,2 -1,3 c-7,0 -12,-5 -12,-12.5z" fill="var(--icon)"/>
      </svg>
      323-555-0148
    </span>
    <span class="contact-row__item">
      <svg class="contact-row__icon" viewBox="0 0 34 26" aria-hidden="true">
        <path d="M0,0 H18 A16,13 0 0 1 18,26 H0 Z" fill="var(--white)"/>
        <rect x="9" y="7.5" width="14" height="11" rx="1.5" fill="none" stroke="var(--icon)" stroke-width="1.6"/>
        <path d="M9.5,8.5 L16,14 L22.5,8.5" fill="none" stroke="var(--icon)" stroke-width="1.6"/>
      </svg>
      info@bramblecrestworks.com
    </span>
  </div>
</article>

<article class="card card--blue">
  <svg class="card__layer" viewBox="0 0 1043 694" preserveAspectRatio="none" aria-hidden="true">
    <polygon points="0,171 1043,462 1043,477 0,186" fill="var(--stripe)"/>
    <polygon points="0,186 1043,477 1043,694 0,694" fill="var(--band)"/>
  </svg>
  <svg class="card__layer" viewBox="0 0 1043 694" preserveAspectRatio="none" role="img" aria-label="Photo of a cracked white model house beside an intact red-roofed model house ringed in red on split ground">
    <defs>
      <radialGradient id="photoRedB" cx="0.75" cy="0.4" r="0.6">
        <stop offset="0" stop-color="var(--photo-red)" stop-opacity=".35"/>
        <stop offset="1" stop-color="var(--photo-light)" stop-opacity="0"/>
      </radialGradient>
      <linearGradient id="photoBaseB" x1="0" y1="0" x2="0" y2="1">
        <stop offset="0" stop-color="var(--white)"/>
        <stop offset="1" stop-color="var(--photo-mid)"/>
      </linearGradient>
    </defs>
    <path d="M540,0 C485,125 560,392 800,396 C900,398 990,394 1043,385 L1043,0 Z" fill="url(#photoBaseB)"/>
    <path d="M540,0 C485,125 560,392 800,396 C900,398 990,394 1043,385 L1043,0 Z" fill="url(#photoRedB)"/>
    <path d="M515,0 C455,130 540,408 800,410 C900,411 990,405 1043,396" fill="none" stroke="var(--brand-blue)" stroke-width="9"/>
    <path d="M540,0 C485,125 560,392 800,396 C900,398 990,394 1043,385" fill="none" stroke="var(--brand-red)" stroke-width="6"/>
  </svg>

  <div class="brand">
    <span class="brand__mark"></span>
    <span class="brand__name">BRAMBLECREST<br>WORKS</span>
  </div>

  <div class="goal-tag">OUR GOAL</div>
  <p class="goal-copy">
    Our primary objective is to empower clients<br>
    with comprehensive knowledge about foundation<br>
    issues and earthquake retrofitting. By educating them on the<br>
    potential risks associated with foundation problems and the importance<br>
    of earthquake retrofitting, we aim to equip homeowners with the necessary<br>
    information to make informed decisions about safeguarding their properties.<br>
    Highlighting the benefits of having their houses properly bolted not only enhances structural<br>
    integrity but also provides peace of mind during seismic events, ensuring the safety and<br>
    security of their homes and loved ones.
  </p>

  <div class="contact-title">
    <span class="contact-title__rule contact-title__rule--left"></span>
    <span>CONTACT US</span>
    <span class="contact-title__rule contact-title__rule--right"></span>
  </div>

  <div class="contact-row">
    <span class="contact-row__item">
      <svg class="contact-row__icon" viewBox="0 0 34 26" aria-hidden="true">
        <path d="M0,0 H18 A16,13 0 0 1 18,26 H0 Z" fill="var(--white)"/>
        <path d="M10,7 l3,-1 2,4 -2,1.5 c1,2.5 2.5,4 4.5,5 l1.5,-2 4,2 -1,3 c-7,0 -12,-5 -12,-12.5z" fill="var(--icon)"/>
      </svg>
      323-555-0148
    </span>
    <span class="contact-row__item">
      <svg class="contact-row__icon" viewBox="0 0 34 26" aria-hidden="true">
        <path d="M0,0 H18 A16,13 0 0 1 18,26 H0 Z" fill="var(--white)"/>
        <rect x="9" y="7.5" width="14" height="11" rx="1.5" fill="none" stroke="var(--icon)" stroke-width="1.6"/>
        <path d="M9.5,8.5 L16,14 L22.5,8.5" fill="none" stroke="var(--icon)" stroke-width="1.6"/>
      </svg>
      info@bramblecrestworks.com
    </span>
  </div>
</article>

</body>
</html>
```